Long term design collaboration - mobile app design & web app design

We are looking for a talented mobile designer to help us improve our UI & UX for mobile app and web app.

The screens that need to be redesigned are attached.

There is potentially a lot more work in future design available for the successful candidate.
The successful candidate would have to take part in daily stand-up around 3 times per week.
The successful candidate would join a dev team
We are software company that does property management

```html
<!DOCTYPE html>
<html lang="en">
<head>
<meta charset="utf-8">
<title>Sending Letter – Overview</title>
<link rel="stylesheet" href="https://fonts.googleapis.com/css2?family=Poppins:wght@400;500;600&display=swap">
<style>
:root{
  --brand:#2659c2;
  --brand-soft:#eef2fd;
  --header-bg:#f1f5fd;
  --page-bg:#f4f4f6;
  --card:#ffffff;
  --ink:#222430;
  --ink-soft:#3a3d48;
  --muted:#6b6e78;
  --warn:#f5a60d;
  --warn-soft:#fdf4e4;
  --warn-circle:#fdefd6;
  --danger:#e8323c;
  --line:#e6e8ee;
}
*{box-sizing:border-box;margin:0;padding:0}
html,body{width:1200px;height:1164px;overflow:hidden}
body{font-family:"Poppins",sans-serif;color:var(--ink);background:var(--page-bg);position:relative}
.abs{position:absolute}

.brand-bar{left:0;top:0;width:240px;height:75px;background:var(--brand);display:flex;align-items:center;padding-left:30px;gap:14px;color:#fff;font-size:20px}
.brand-mark{width:16px;height:16px;background:#fff;border-radius:3px}

.sidebar{left:0;top:75px;width:240px;height:1089px;background:#fff}
.nav-item{position:absolute;left:16px;width:207px;height:30px;display:flex;align-items:center;padding-left:14px;font-size:12px;color:var(--muted);border-radius:3px}
.nav-item .ico{width:15px;height:15px;margin-right:12px}
.nav-item .chev{position:absolute;right:14px;top:9px}
.nav-item.active{background:var(--brand-soft);color:var(--brand)}

.topbar{left:240px;top:0;width:960px;height:75px;background:var(--header-bg);border-bottom:1px solid var(--line)}
.page-title{left:270px;top:22px;font-size:24px;color:var(--brand);font-weight:400}
.bell{left:982px;top:27px}
.avatar{left:1015px;top:24px;width:27px;height:27px;border-radius:50%;border:1px solid #d5daea;background:#fff;display:flex;align-items:center;justify-content:center}
.account{left:1052px;top:22px;color:var(--brand);font-size:13px;line-height:16px}
.account small{display:block;font-size:9.5px;color:var(--muted);line-height:13px}

.section-heading{left:270px;top:104px;font-size:17px;color:var(--brand)}

.card{position:absolute;background:var(--card);border-radius:12px}
.card-title{position:absolute;left:24px;font-size:16px;font-weight:500;color:var(--ink-soft)}

.btn{position:absolute;background:var(--brand);color:#fff;font-size:12px;font-weight:500;border-radius:4px;display:flex;align-items:center;justify-content:center}
.toggle{position:absolute;border:1px solid #c9d1e6;border-radius:5px;display:flex;align-items:center;padding:3px;gap:4px}
.toggle span{height:27px;display:flex;align-items:center;padding:0 9px;font-size:12px;font-weight:500;color:var(--muted);border-radius:3px}
.toggle .on{background:var(--brand);color:#fff}

.setup-pill{position:absolute;top:77.5px;width:190px;height:58.5px;background:var(--warn-soft);border:1px solid var(--warn);border-radius:6px;padding:9px 12px;font-size:13px;line-height:20px;color:var(--ink-soft)}
.setup-pill svg{position:absolute;right:17px;top:16px}

.tile{position:absolute;width:190px;height:82px;background:#fff;border-radius:6px;box-shadow:0 1px 4px rgba(30,40,70,.12);padding:8px 12px}
.tile h4{font-size:13px;font-weight:600;line-height:18px}
.tile p{margin-top:18px;font-size:13px;line-height:20px;color:var(--ink-soft)}
.tile .badge{position:absolute;right:12px;top:7px;width:28px;height:28px;border-radius:50%;background:var(--warn-circle);display:flex;align-items:center;justify-content:center}
.tile .status{position:absolute;right:11px;top:10px}
.tile.tall{height:91px}
.tile.big h4{font-size:17px;font-weight:500}
.tile.big p{margin-top:12px}
</style>
</head>
<body>

<div class="abs brand-bar"><span class="brand-mark"></span>logo</div>

<nav class="abs sidebar">
  <svg width="0" height="0" style="position:absolute">
    <defs>
      <g id="grid"><rect x="0" y="0" width="6.5" height="6.5" rx="2"/><rect x="8.5" y="0" width="6.5" height="6.5" rx="2"/><rect x="0" y="8.5" width="6.5" height="6.5" rx="2"/><rect x="8.5" y="8.5" width="6.5" height="6.5" rx="2"/></g>
      <path id="chev" d="M1 1l4 4-4 4" fill="none" stroke-width="1.3" stroke-linecap="round" stroke-linejoin="round"/>
    </defs>
  </svg>
  <div class="nav-item" style="top:41px"><svg class="ico" fill="#9a9ca4"><use href="#grid"/></svg>User Directories<svg class="chev" width="7" height="10" stroke="#7a7d86"><use href="#chev"/></svg></div>
  <div class="nav-item" style="top:73px"><svg class="ico" fill="#9a9ca4"><use href="#grid"/></svg>Switch Development<svg class="chev" width="7" height="10" stroke="#7a7d86"><use href="#chev"/></svg></div>
  <div class="nav-item" style="top:104px"><svg class="ico" fill="#9a9ca4"><use href="#grid"/></svg>Service Change<svg class="chev" width="7" height="10" stroke="#7a7d86"><use href="#chev"/></svg></div>
  <div class="nav-item" style="top:136px"><svg class="ico" fill="#9a9ca4"><use href="#grid"/></svg>Property Balance<svg class="chev" width="7" height="10" stroke="#7a7d86"><use href="#chev"/></svg></div>
  <div class="nav-item active" style="top:173px"><svg class="ico" fill="#2659c2"><use href="#grid"/></svg>Sending Letter<svg class="chev" width="7" height="10" stroke="#2659c2"><use href="#chev"/></svg></div>
  <div class="nav-item" style="top:211px"><svg class="ico" fill="#9a9ca4"><use href="#grid"/></svg>Regular Services<svg class="chev" width="7" height="10" stroke="#7a7d86"><use href="#chev"/></svg></div>
</nav>

<header class="abs topbar"></header>
<h1 class="abs page-title">Sending Letter</h1>
<svg class="abs bell" width="18" height="20" viewBox="0 0 18 20"><path d="M9 2a5.5 5.5 0 0 0-5.5 5.5v3.8L2 14h14l-1.5-2.7V7.5A5.5 5.5 0 0 0 9 2z" fill="#2659c2"/><path d="M6.5 16a2.5 2.5 0 0 0 5 0z" fill="#2659c2"/><circle cx="15" cy="3" r="2.5" fill="#2659c2" stroke="#f1f5fd" stroke-width="1.2"/></svg>
<div class="abs avatar"><svg width="13" height="14" viewBox="0 0 13 14"><circle cx="6.5" cy="4" r="3.2" fill="#2659c2"/><path d="M0.8 13.5a5.7 5.2 0 0 1 11.4 0z" fill="#2659c2"/></svg></div>
<div class="abs account">Rohan Mehta<small>My Account</small></div>

<h2 class="abs section-heading">Overview</h2>

<svg width="0" height="0" style="position:absolute"><defs>
  <g id="arrow"><path d="M2 12L12 2M4.5 2H12v7.5" fill="none" stroke="#f5a60d" stroke-width="2.2" stroke-linecap="round" stroke-linejoin="round"/></g>
</defs></svg>

<section class="card" style="left:270px;top:151.5px;width:900px;height:160px">
  <h3 class="card-title" style="top:28px">Please Complete basic setup</h3>
  <svg class="abs" style="left:270px;top:27px" width="25" height="25" viewBox="0 0 25 25"><circle cx="12.5" cy="12.5" r="11.3" fill="none" stroke="#f5a60d" stroke-width="1.8"/><path d="M12.5 6.5v8" stroke="#f5a60d" stroke-width="1.8" stroke-linecap="round"/><circle cx="12.5" cy="18" r="1.2" fill="#f5a60d"/></svg>
  <div class="btn" style="left:790.5px;top:24px;width:85.5px;height:30px">Overview</div>
  <div class="setup-pill" style="left:24px">Service Charge<br>Schedules<svg width="14" height="14"><use href="#arrow"/></svg></div>
  <div class="setup-pill" style="left:244.5px">Service Charge<br>Apprtionment<svg width="14" height="14"><use href="#arrow"/></svg></div>
  <div class="setup-pill" style="left:465px">Invite Residents<br>&amp; Leaseholder<svg width="14" height="14"><use href="#arrow"/></svg></div>
  <div class="setup-pill" style="left:685.5px">Connect Payment<br>Provider<svg width="14" height="14"><use href="#arrow"/></svg></div>
</section>

<section class="card" style="left:270px;top:330px;width:900px;height:200px">
  <h3 class="card-title" style="top:30px;font-size:17.5px">General</h3>
  <div class="toggle" style="left:706px;top:24px;width:170px;height:36px"><span class="on">Overview</span><span>Overview</span></div>
  <div class="tile" style="left:24px;top:84px"><h4>Units</h4><p>85</p><span class="badge"><svg width="14" height="14"><use href="#arrow"/></svg></span></div>
  <div class="tile" style="left:244.5px;top:84px"><h4>Handover</h4><p>12 January 2023</p><span class="badge"><svg width="14" height="14"><use href="#arrow"/></svg></span></div>
  <div class="tile tall" style="left:465px;top:84px"><h4>Address</h4><p>42 Linden Grove Terrace,<br>London, N4 2QT</p><span class="badge"><svg width="14" height="14"><use href="#arrow"/></svg></span></div>
  <div class="tile" style="left:685.5px;top:84px"><h4>Section 20 Limit</h4><p>$ 25</p></div>
</section>

<section class="card" style="left:270px;top:547.5px;width:960px;height:186px">
  <h3 class="card-title" style="top:24px;font-size:17.5px">Compliance</h3>
  <div class="tile" style="left:24px;top:70px"><h4>Asbestos</h4><p>NA</p></div>
  <div class="tile" style="left:229.5px;top:70px"><h4>Legislation</h4><p>-</p>
    <svg class="status" width="25" height="25" viewBox="0 0 25 25"><circle cx="12.5" cy="12.5" r="11.3" fill="none" stroke="#f5a60d" stroke-width="1.7"/><path d="M9.3 9.5a3.2 3.2 0 1 1 4.5 2.9c-.9.4-1.3 1-1.3 2v.8" fill="none" stroke="#f5a60d" stroke-width="1.7" stroke-linecap="round"/><circle cx="12.5" cy="18.3" r="1.1" fill="#f5a60d"/></svg></div>
  <div class="tile tall" style="left:435px;top:70px"><h4>Drains</h4><p>Overdue<br>10 December 2023</p>
    <svg class="status" width="25" height="25" viewBox="0 0 25 25"><circle cx="12.5" cy="12.5" r="11.3" fill="none" stroke="#e8323c" stroke-width="1.7"/><path d="M12.5 6.5v8" stroke="#e8323c" stroke-width="1.8" stroke-linecap="round"/><circle cx="12.5" cy="18" r="1.2" fill="#e8323c"/></svg></div>
  <div class="tile" style="left:640.5px;top:70px"><h4>Gutters</h4><p>NA</p></div>
  <div class="tile" style="left:846px;top:70px"><h4>Dry Risers</h4><p>NA</p></div>
</section>

<section class="card" style="left:270px;top:751.5px;width:960px;height:177px">
  <h3 class="card-title" style="top:24px;font-size:17.5px">Insurances</h3>
  <div class="tile" style="left:24px;top:70.5px"><h4>Terrorism</h4><p>NA</p></div>
  <div class="tile" style="left:229.5px;top:70.5px"><h4>Building</h4><p>NA</p></div>
  <div class="tile" style="left:435px;top:70.5px;height:71px"><h4>Engineering</h4><p>NA</p></div>
  <div class="tile" style="left:640.5px;top:70.5px"><h4>D &amp; O</h4><p>NA</p></div>
  <div class="tile big" style="left:846px;top:70.5px"><h4>Reinstatement</h4><p>NA</p></div>
</section>

<section class="card" style="left:270px;top:946.5px;width:441px;height:177px">
  <h3 class="card-title" style="top:24px;font-size:17.5px">Service Charge</h3>
  <div class="tile" style="left:24px;top:70.5px"><h4>Year End</h4><p>24/12/2024</p></div>
  <div class="tile" style="left:229.5px;top:70.5px"><h4>Demand Dates</h4><p>NA</p></div>
</section>

<section class="card" style="left:729px;top:946.5px;width:441px;height:177px">
  <h3 class="card-title" style="top:24px;font-size:17.5px">Cosec</h3>
  <div class="tile" style="left:24px;top:70.5px"><h4>Are We Responsible</h4><p>No</p></div>
</section>

</body>
</html>
```